Business Card Design

We are a florist shop that also stocks a range of giftware and jewellery. I would like a new design that incorporates a light green background. If you could use a skeleton leaf somewhere in the design that would be great. I would also like to incorporate the find us on Chatterlink logo on this design.

Industry/Entity Type

Florist

Contact Information for Business Card

Petals at Harwick
42 Tellbury street
Brenlow Victoria 3947
Phone: 0352984407
Fax : 0352984433
email: pah@brightmail.net.au

Proprietors : Dana & Lou Fenwright

```html
<!DOCTYPE html>
<html lang="en">
<head>
<meta charset="utf-8">
<title>Petals at Harwick – Business Card</title>
<link rel="stylesheet" href="https://fonts.googleapis.com/css2?family=Source+Sans+3:wght@400;600&display=swap">
<style>
  :root {
    --backdrop-light: #5a5a5a;
    --backdrop-dark: #2e2e2e;
    --green-deep: #0b7d43;
    --green-mid: #00a651;
    --green-bright: #6cbf45;
    --green-brand: #0e6b3a;
    --olive-band: #3c4320;
    --lime-band: #bed22e;
    --card-white: #ffffff;
    --card-tint: #b3d889;
    --ink: #111111;
    --flower-tone: #d9d6c6;
    --swirl-tone: #3cb54a;
  }
  * { margin: 0; padding: 0; box-sizing: border-box; }
  html, body { width: 1200px; height: 999px; overflow: hidden; }
  body {
    position: relative;
    background: radial-gradient(ellipse at 50% 45%, var(--backdrop-light) 0%, var(--backdrop-dark) 100%);
    font-family: "Source Sans 3", "Myriad Pro", Arial, sans-serif;
    color: var(--ink);
  }
  .card {
    position: absolute;
    left: 68px; top: 192px;
    width: 1063px; height: 614px;
    background: linear-gradient(to bottom, var(--card-white) 0%, var(--card-white) 50%, var(--card-tint) 100%);
    overflow: hidden;
  }
  .card-waves { position: absolute; left: 0; top: 0; width: 1063px; height: 320px; }
  .flower-art {
    position: absolute; left: 0; top: 10px; width: 225px; height: 210px;
    border-radius: 48% 52% 55% 45%;
    background: radial-gradient(circle at 40% 40%, #f1efe6 0%, var(--flower-tone) 70%, rgba(217,214,198,0) 100%);
  }
  .swirl-art {
    position: absolute; left: 250px; top: 60px; width: 360px; height: 245px;
    border-radius: 50%;
    background: radial-gradient(ellipse at 50% 45%, rgba(60,181,74,0.55) 0%, rgba(60,181,74,0) 70%);
  }
  .brand-name {
    position: absolute; left: 32px; top: 308px;
    font-size: 64px; font-weight: 400; line-height: 1.0;
    color: var(--green-brand);
  }
  .brand-name .second-line { display: block; padding-left: 78px; }
  .proprietors {
    position: absolute; left: 45px; top: 512px;
    font-size: 34px; font-weight: 400;
  }
  .divider {
    position: absolute; left: 649px; top: 336px;
    width: 2px; height: 238px;
    background: linear-gradient(to bottom, rgba(17,17,17,0.2), var(--ink) 20%, var(--ink) 80%, rgba(17,17,17,0.2));
  }
  .address {
    position: absolute; left: 696px; top: 330px;
    font-size: 28px; line-height: 37.5px; font-style: normal;
  }
  .contacts {
    position: absolute; left: 694px; top: 460px;
    list-style: none; font-size: 28px; line-height: 38px;
  }
  .contacts li { display: flex; align-items: center; }
  .contacts svg { width: 26px; height: 26px; margin-right: 38px; flex: none; }
</style>
</head>
<body>
  <section class="card" aria-label="Petals at Harwick business card">
    <svg class="card-waves" viewBox="0 0 1063 320" aria-hidden="true">
      <defs>
        <linearGradient id="topGreen" x1="0" x2="1" y1="0" y2="0">
          <stop offset="0" stop-color="var(--green-deep)"/>
          <stop offset="0.65" stop-color="var(--green-mid)"/>
          <stop offset="1" stop-color="var(--green-bright)"/>
        </linearGradient>
      </defs>
      <path d="M0,0 H1063 V62 C950,56 880,192 760,192 C650,192 600,138 450,134 C300,130 160,214 0,212 Z" fill="url(#topGreen)"/>
      <path d="M0,150 C120,120 220,180 300,130" fill="none" stroke="var(--card-white)" stroke-width="10"/>
      <path d="M0,198 C160,200 300,124 450,138 C600,150 650,198 760,196 C880,196 950,66 1063,76" fill="none" stroke="var(--olive-band)" stroke-width="16"/>
      <path d="M0,226 C160,232 300,152 450,166 C600,176 650,214 760,212 C880,212 950,84 1063,90" fill="none" stroke="var(--lime-band)" stroke-width="14"/>
      <path d="M760,190 C880,188 950,64 1063,66" fill="none" stroke="var(--card-white)" stroke-width="3"/>
    </svg>
    <div class="flower-art" role="img" aria-label="Illustration of two white blossoms with yellow centres"></div>
    <div class="swirl-art" role="img" aria-label="Decorative green flourish of curling vines"></div>

    <h1 class="brand-name">Petals at<span class="second-line">Harwick</span></h1>
    <p class="proprietors">Dana &amp; Lou Fenwright</p>

    <div class="divider"></div>

    <address class="address">
      Petals at Harwick<br>
      42 Tellbury street<br>
      Brenlow Victoria 3947
    </address>

    <ul class="contacts">
      <li>
        <svg viewBox="0 0 24 24" aria-label="Phone"><path d="M6.6 3.5l3 3.4-1.8 2.2c1 2.2 2.9 4.1 5.1 5.1l2.2-1.8 3.4 3-1.6 2.9C11.5 18.6 5.4 12.5 5.7 5.1z" fill="var(--ink)"/><path d="M14 3a7 7 0 0 1 7 7M14 6.5a3.5 3.5 0 0 1 3.5 3.5" fill="none" stroke="var(--ink)" stroke-width="1.8"/></svg>
        <span>0352984407</span>
      </li>
      <li>
        <svg viewBox="0 0 24 24" aria-label="Fax"><rect x="7" y="2" width="10" height="8" fill="var(--ink)"/><rect x="3" y="10" width="18" height="8" rx="1" fill="var(--ink)"/><rect x="6" y="19" width="12" height="3" fill="var(--ink)"/><rect x="8" y="12" width="8" height="2" fill="#fff"/></svg>
        <span>0352984433</span>
      </li>
      <li>
        <svg viewBox="0 0 24 24" aria-label="Email"><path d="M2 10l10-7 10 7v11H2z" fill="var(--ink)"/><path d="M4 10l8 6 8-6" fill="none" stroke="#fff" stroke-width="1.6"/></svg>
        <span>pah@brightmail.net.au</span>
      </li>
    </ul>
  </section>
</body>
</html>
```